Brochure Design Project (Design Studio)

Items required:
1-Brochure. We suggest 15Cm X 15 Cm after cutting.
2-Business Card.
3-Head letter.
4-Folder ( folder should carry the Brochure in pocket and the business card in a pocket on the opposite side of the folder.
5-Envelope to carry everything.
This brochure is expected to draw attention of high level management in companies to the quality and creativity of the design work and encourage them to do business with us. note that brochure will be printed in high quality printing and paper.
The game plan is as follows:
Over all description, the theme of the brochure is drawn from the website theme (website will be uploaded shortly, pictures of the website are attached, logo appears in the top left corner). Please avoid direct copying from the website unless it is a creative copying, just draw the theme from there. however, we need it to be elegant, stylish and class in colors and style. This is a MUST.
Furthermore, the main items of the Brochure:
1-The Studio is not just a studio: we will take about how Branding. A file is attached of the content. (slight changes/modification can apply during the designing process)
2-The Process: this one has to be a visual illustration of the process, it has to be very creative, could be elegant arrows and comics, could be elegant drawing, could be an elegant icons. The drawing should be separate from the steps, we need to the drawing and we need to have the steps listed and commentary, or if want to integrate both in one in an artistic way. Just don’t lose track of the theme and elegance. (steps and commentary are attached, slight changes/modification can apply at anytime.
3-Our Team: another drawing of your suggestion to illustrate the team members, we need to include the names and designation as well leave a place for some of them to say what they need to say about their style of designing. I leave it for your imagination to put this all together in a nice attractive visual illustration.
4-Works: this section will generally show the works of our designers. It needs to be focused on the works themselves, client should be able to view the details of the works ( note that when it comes to brochures and websites, we don’t need to reach to the extent with which the client can read the text in those pictures of the website or brochure, but still can see the overall design clearly). Each design is to carry the name of the designer. Last thing, this section will classify works into categories, like, Brochures, Corporate identity, print design. We didn’t finalize those categories, we will provide them to you shortly, last thing to be said, we are planning to include around 25-30 designs of each sub-category, eg. Corporate identity will have 30 business card s designs and 30 stationary designs.
5-Contacts: the company contacts.
We the brochure after printing should be 15x15 Cm.
Creativity and art work is a major player in selection.
general managers, owners
Printing

```html
<!DOCTYPE html>
<html lang="en">
<head>
<meta charset="utf-8">
<title>Verandel Studio — Branding Brochure</title>
<link rel="stylesheet" href="https://fonts.googleapis.com/css2?family=Questrial&family=Raleway:wght@300&family=Yanone+Kaffeesatz:wght@500&display=swap">
<style>
  :root {
    --canvas: #ffffff;
    --ink: #3e4a4f;
    --grey-page: #9a9f97;
    --grey-strip: #7d827b;
    --charcoal: #555557;
    --deep-red: #8e0000;
    --crimson: #c8102e;
    --lime: #c6f03c;
    --white: #ffffff;
    --photo-wall: #d9ddd8;
    --photo-red: #c0163a;
  }
  * { box-sizing: border-box; margin: 0; padding: 0; }
  html, body { width: 1200px; height: 622px; overflow: hidden; background: var(--canvas); }
  body { position: relative; font-family: "Questrial", "Century Gothic", sans-serif; }

  .page { position: absolute; top: 68px; width: 495px; height: 494px; overflow: hidden; }
  .page--cover { left: 85px; background: var(--white); border: 1px solid #cfcfcf; }
  .page--branding { left: 621px; background: var(--grey-page); }

  /* Cover */
  .cover__photo {
    position: absolute; left: 0; top: 0; width: 100%; height: 310px;
    background:
      radial-gradient(ellipse 40% 55% at 62% 40%, var(--photo-red) 0%, rgba(192,22,58,0.85) 45%, rgba(192,22,58,0) 75%),
      radial-gradient(ellipse 60% 70% at 30% 50%, #eef0ec 0%, var(--photo-wall) 70%, #b7bfbb 100%);
  }
  .cover__brand {
    position: absolute; left: 0; top: 310px; width: 100%; height: 54px;
    display: flex; align-items: center; justify-content: center;
  }
  .brand-name { font-family: "Questrial", sans-serif; color: var(--ink); font-size: 24px; letter-spacing: 1px; }
  .cover__band {
    position: absolute; left: 0; top: 364px; width: 100%; height: 130px;
    background: linear-gradient(90deg, var(--charcoal) 0%, #6d4a4a 45%, var(--deep-red) 100%);
  }
  .cover__slogan {
    position: absolute; right: 16px; bottom: 14px;
    font-family: "Raleway", sans-serif; font-weight: 300; color: var(--white); font-size: 22px;
  }

  /* Branding page */
  .branding__strip { position: absolute; left: 0; top: 0; width: 100%; height: 8px; background: var(--grey-strip); }
  .branding__header {
    position: absolute; left: 0; top: 8px; width: 100%; height: 54px; background: var(--white);
    display: flex; align-items: center; justify-content: flex-end; padding-right: 22px;
  }
  .tag {
    position: absolute; left: 10px; top: 14px; width: 118px; height: 38px;
    background: linear-gradient(180deg, #b31616 0%, #6e0b0b 100%);
    border-radius: 5px; transform: rotate(-12deg);
    color: var(--white); font-size: 20px; display: flex; align-items: center; justify-content: center;
    box-shadow: 0 3px 5px rgba(0,0,0,0.35);
  }
  .branding__intro {
    position: absolute; left: 14px; top: 90px; width: 468px;
    color: var(--white); font-size: 11.3px; line-height: 16.6px;
  }
  .branding__intro .highlight { color: var(--crimson); }

  .column { position: absolute; top: 300px; width: 230px; }
  .column--strong { left: 12px; }
  .column--benefits { left: 261px; }
  .column__title {
    font-family: "Yanone Kaffeesatz", sans-serif; font-weight: 500;
    color: var(--crimson); font-size: 26px; line-height: 26px;
  }
  .column__subtitle {
    font-family: "Yanone Kaffeesatz", sans-serif; font-weight: 500;
    color: var(--crimson); font-size: 17px; line-height: 18px;
  }
  .column__list { list-style: none; margin-top: 6px; color: var(--white); font-size: 11.3px; line-height: 19.6px; }
  .column__list li::before { content: "•"; margin: 0 7px 0 4px; }
  .column--benefits .column__list { margin-top: 8px; }
  .arrow { position: absolute; width: 60px; height: 78px; }
  .arrow--strong { left: 146px; top: 312px; }
  .arrow--benefits { left: 425px; top: 312px; }

  .branding__closing {
    position: absolute; left: 14px; top: 444px; width: 470px;
    color: var(--lime); font-size: 16.5px; line-height: 21px; font-style: italic;
  }
</style>
</head>
<body>

<section class="page page--cover">
  <div class="cover__photo" role="img" aria-label="Fashion photograph: a model in a red dress whose fabric dissolves into red paint splashes against a pale textured wall"></div>
  <div class="cover__brand"><span class="brand-name">Verandel Studio</span></div>
  <div class="cover__band">
    <p class="cover__slogan">Personify your business</p>
  </div>
</section>

<section class="page page--branding">
  <div class="branding__strip"></div>
  <header class="branding__header"><span class="brand-name">Verandel Studio</span></header>
  <div class="tag">Branding!</div>

  <div class="branding__intro">
    <p>Do you prefer to work with specific Individuals over others? Do you feel that working with those individuals give you the peace of mind because you know that they are Enthusiastic, ethical, Goal Focused, Committed, Disciplined, creative, visionary and self-aware?</p>
    <p>Well, probably you like to work with companies of the same qualities as those persons! COMPANIES HAVE PERSONALITIES TOO.</p>
    <p>Branding is your vehicle to deliver the traits of your company to the audience. Branding assist you to control the perception of company among public.</p>
    <p>If you are very organized company, deliver on time, committed to your clients, produce quality products to the highest standards. <span class="highlight">Branding is the key to make the public hear and believe those qualities and consider your products as their 1st choice.</span></p>
  </div>

  <div class="column column--strong">
    <h2 class="column__title">Strong Branding</h2>
    <p class="column__subtitle">Means your company is:</p>
    <ul class="column__list">
      <li>Large and established.</li>
      <li>A synonym of Quality.</li>
      <li>Experienced and reliable.</li>
    </ul>
  </div>

  <div class="column column--benefits">
    <h2 class="column__title">Branding gives you:</h2>
    <ul class="column__list">
      <li>Loyalty and advocacy.</li>
      <li>Influence of choice.</li>
      <li>Command a price premium.</li>
      <li>Uniqueness.</li>
      <li>Growth of your business and products.</li>
    </ul>
  </div>

  <svg class="arrow arrow--strong" viewBox="0 0 60 78" aria-hidden="true">
    <defs>
      <linearGradient id="arrowFill" x1="0" y1="0" x2="1" y2="1">
        <stop offset="0" stop-color="#5a5a5a"/>
        <stop offset="1" stop-color="#b01010"/>
      </linearGradient>
    </defs>
    <path d="M8 14 C30 2 58 14 54 42 C52 54 46 62 40 66 L44 74 L20 70 L30 50 L34 58 C40 52 42 44 40 36 C36 22 22 18 12 24 Z"
          fill="url(#arrowFill)" stroke="#ffffff" stroke-width="3" stroke-linejoin="round"/>
  </svg>
  <svg class="arrow arrow--benefits" viewBox="0 0 60 78" aria-hidden="true">
    <path d="M8 14 C30 2 58 14 54 42 C52 54 46 62 40 66 L44 74 L20 70 L30 50 L34 58 C40 52 42 44 40 36 C36 22 22 18 12 24 Z"
          fill="url(#arrowFill)" stroke="#ffffff" stroke-width="3" stroke-linejoin="round"/>
  </svg>

  <p class="branding__closing">We are more than just a creative studio; we can personify your business and dress to impress!</p>
</section>

</body>
</html>
```